Mellow Truffles. We need a website as delcious as our chocolate.

I need a website to promote our humble chocolate business. We our proud of are chocolate because we use only our favorite ingredients. We believe in originality and complete enjoyment of our chocolates. I am looking for a sleek and smooth website. I would like to see typical pages such as contact information and an intro. I would like to have a product page, which can be easily updated with photos of new chocolate. I would also like to see a page where we can educate customers about chocolate. This might be tricky but I would like our customers to leave the site knowing they are getting great chocolate! I have a logo and general color scheme, which I will try to upload somewhere. I looking for an original and exciting website.
Updates

Websites we like:

1. http://www.paul-van-orlen.example/ (looks really good)

2. http://www.tremilcocoa.example/

uploaded logo !

Target Market(s)

People who enjoy chocolate.

Industry/Entity Type

Business

Requirements
Must have
• User Friendly
Page were pictures of new chocolate can be easily updated.

Nice to have
• Calming and appetizing music
Section where recent tweets can show up on the site.

```html
<!DOCTYPE html>
<html lang="en">
<head>
<meta charset="utf-8">
<title>Mellow Truffles — Homemade Chocolate</title>
<link rel="stylesheet" href="https://fonts.googleapis.com/css2?family=Open+Sans:wght@400&family=Tinos:ital,wght@0,400;1,400&family=Lora:ital,wght@1,700&display=swap">
<style>
  :root {
    --cocoa-deep: #2a0d04;
    --cocoa-dark: #3d1608;
    --cocoa-mid: #6b2e10;
    --caramel: #b4703a;
    --caramel-light: #e0a46a;
    --panel-bg: #220b04;
    --nav-ink: #2b1108;
    --heading-ink: #dcbf9f;
    --body-ink: #efe4d8;
    --link-ink: #c58a58;
    --footer-ink: #e9ccaa;
  }
  html, body {
    margin: 0;
    padding: 0;
    overflow: hidden;
    background: var(--cocoa-deep);
  }
  .page {
    position: relative;
    width: 1200px;
    height: 812px;
    overflow: hidden;
    background: radial-gradient(ellipse at 85% 45%, #8a4518 0%, #4a1a08 55%, var(--cocoa-deep) 100%);
    font-family: "Tinos", "Times New Roman", serif;
  }
  .backdrop {
    position: absolute;
    inset: 0;
  }
  .brand {
    position: absolute;
    left: 190px;
    top: 84px;
    width: 190px;
    height: 96px;
    display: flex;
    align-items: center;
    justify-content: center;
    border-radius: 50%;
    background: radial-gradient(ellipse at center, rgba(235,220,205,0.85) 0%, rgba(200,170,150,0.45) 50%, rgba(120,60,30,0) 75%);
  }
  .brand-name {
    margin: 0;
    font-family: "Tinos", "Times New Roman", serif;
    font-weight: 400;
    font-size: 27px;
    color: var(--nav-ink);
  }
  .main-nav a {
    position: absolute;
    font-family: "Open Sans", Verdana, sans-serif;
    font-size: 16px;
    color: var(--nav-ink);
    text-decoration: none;
  }
  .nav-home { left: 606px; top: 86px; }
  .nav-about { left: 686px; top: 65px; }
  .nav-products { left: 796px; top: 51px; }
  .nav-contacts { left: 912px; top: 46px; }
  .shop-gallery {
    position: absolute;
    left: 160px;
    top: 105px;
    width: 575px;
    height: 640px;
  }
  .welcome-panel {
    position: absolute;
    left: 740px;
    top: 88px;
    width: 302px;
    height: 544px;
    background: var(--panel-bg);
    border-radius: 4px;
    box-shadow: 0 0 14px rgba(0,0,0,0.6);
  }
  .welcome-title {
    position: absolute;
    left: 14px;
    top: 38px;
    margin: 0;
    font-family: "Lora", Georgia, serif;
    font-style: italic;
    font-weight: 700;
    font-size: 19px;
    color: var(--heading-ink);
  }
  .welcome-rule {
    position: absolute;
    left: 14px;
    top: 69px;
    width: 266px;
    height: 1px;
    background: #4a2414;
  }
  .welcome-text {
    position: absolute;
    left: 15px;
    top: 74px;
    width: 272px;
    margin: 0;
    font-size: 15px;
    line-height: 25px;
    color: var(--body-ink);
  }
  .more-link {
    font-size: 15px;
    text-decoration: underline;
    color: var(--link-ink);
  }
  .welcome-text .more-link {
    float: right;
    margin-right: 6px;
  }
  .feature-photo {
    position: absolute;
    left: 17px;
    top: 237px;
    width: 262px;
    height: 295px;
    border-radius: 10px;
    background: radial-gradient(ellipse at 45% 65%, #e8d2b8 0%, #b88a58 40%, #6a3a18 100%);
  }
  .feature-photo .more-link {
    position: absolute;
    right: 7px;
    bottom: 17px;
    color: #f5ece2;
  }
  .site-footer {
    position: absolute;
    left: 827px;
    top: 676px;
    font-style: italic;
    font-size: 15px;
    color: var(--footer-ink);
  }
</style>
</head>
<body>
<div class="page">
  <svg class="backdrop" width="1200" height="812" viewBox="0 0 1200 812" aria-hidden="true">
    <defs>
      <linearGradient id="copperBand" x1="0" y1="0" x2="1" y2="0">
        <stop offset="0" stop-color="#5a2209"/>
        <stop offset="0.35" stop-color="#c9894f"/>
        <stop offset="0.7" stop-color="#8a4519"/>
        <stop offset="1" stop-color="#d69a5e"/>
      </linearGradient>
      <linearGradient id="darkBand" x1="0" y1="0" x2="0" y2="1">
        <stop offset="0" stop-color="#4a1a08"/>
        <stop offset="1" stop-color="#1e0803"/>
      </linearGradient>
    </defs>
    <path d="M0 0 H1200 V20 C1000 -10 800 40 600 40 C400 40 200 -10 0 20 Z" fill="#2a0d04"/>
    <path d="M0 30 C200 -10 420 60 640 45 C860 30 1000 0 1200 25 V90 C1000 60 860 95 640 110 C420 125 200 70 0 100 Z" fill="url(#copperBand)" opacity="0.85"/>
    <path d="M0 95 C200 70 420 125 640 115 C860 100 1000 70 1200 90 V120 C1000 95 820 130 640 140 C420 150 200 100 0 125 Z" fill="url(#darkBand)"/>
    <path d="M0 120 C150 100 300 160 480 185 C600 200 700 170 740 150 L740 120 C700 140 600 165 480 150 C300 130 150 80 0 95 Z" fill="#3d1608"/>
    <path d="M0 610 C250 700 500 740 800 680 C1000 640 1100 630 1200 650 V812 H0 Z" fill="url(#darkBand)"/>
    <path d="M0 660 C250 750 520 780 820 720 C1000 685 1120 680 1200 700 V740 C1100 720 1000 730 820 765 C520 820 250 790 0 720 Z" fill="url(#copperBand)" opacity="0.8"/>
    <path d="M0 750 C300 812 600 800 900 780 C1050 770 1150 775 1200 780 V812 H0 Z" fill="#1e0803"/>
  </svg>

  <div class="brand">
    <h1 class="brand-name">Mellow Truffles</h1>
  </div>

  <nav class="main-nav">
    <a class="nav-home" href="#">home</a>
    <a class="nav-about" href="#">about us</a>
    <a class="nav-products" href="#">products</a>
    <a class="nav-contacts" href="#">contacts</a>
  </nav>

  <svg class="shop-gallery" width="575" height="640" viewBox="0 0 575 640" role="img" aria-label="Three panels showing the chocolate shop: a chocolatier packing boxes, the display counter, and the shop front">
    <defs>
      <linearGradient id="galleryLeft" x1="0" y1="0" x2="0" y2="1">
        <stop offset="0" stop-color="#cfd2cc"/>
        <stop offset="0.4" stop-color="#3c8a94"/>
        <stop offset="1" stop-color="#4a3a30"/>
      </linearGradient>
      <linearGradient id="galleryMid" x1="0" y1="0" x2="0" y2="1">
        <stop offset="0" stop-color="#3a302a"/>
        <stop offset="0.45" stop-color="#8a7a6a"/>
        <stop offset="1" stop-color="#221a16"/>
      </linearGradient>
      <linearGradient id="galleryRight" x1="0" y1="0" x2="0" y2="1">
        <stop offset="0" stop-color="#1a1a1c"/>
        <stop offset="0.45" stop-color="#4a6a66"/>
        <stop offset="1" stop-color="#18181a"/>
      </linearGradient>
    </defs>
    <path d="M5 82 C60 100 130 108 185 100 L185 627 C130 630 60 630 5 625 Z" fill="url(#galleryLeft)"/>
    <path d="M187 100 C260 95 330 80 380 68 L380 580 C320 605 260 615 187 627 Z" fill="url(#galleryMid)"/>
    <path d="M382 68 C450 45 520 20 565 8 L565 525 C510 545 450 565 382 580 Z" fill="url(#galleryRight)"/>
    <path d="M5 82 C60 100 130 108 185 100 C260 95 330 80 380 68 C450 45 520 20 565 8 L565 525 C510 545 450 565 382 580 C320 605 260 615 187 627 C130 630 60 630 5 625 Z" fill="none" stroke="#9a5526" stroke-width="3"/>
    <line x1="186" y1="100" x2="186" y2="627" stroke="#9a5526" stroke-width="2"/>
    <line x1="381" y1="68" x2="381" y2="580" stroke="#9a5526" stroke-width="2"/>
  </svg>

  <section class="welcome-panel">
    <h2 class="welcome-title">Welcome to our site</h2>
    <div class="welcome-rule"></div>
    <p class="welcome-text">I need a website to promote our humble chocolate business. We our proud of are chocolate because we use only our favorite ingredients. We believe in originality and complete enjoyment of our chocolates. <a class="more-link" href="#">&gt;&gt; More</a></p>
    <div class="feature-photo" role="img" aria-label="A bag of homemade chocolates wrapped in cellophane with a ribbon">
      <a class="more-link" href="#">&gt;&gt; More</a>
    </div>
  </section>

  <footer class="site-footer">2012 | copyright | Privacy Policy</footer>
</div>
</body>
</html>
```